4' x 8' Construction Project Sign, think of a very large business card

We need project signs for our construction sites, the sign will be mounted along the road so cars driving by can quickly read. the sign should be able to be read as cars drive by doing highway speed.

Think like your making a large business card

I would like to include "NOW HIRING" Superintendents, Project Managers, Pipe Foremen, Pipe Layers, and Equipment Operators

Description of services we provide should include

Civil Construction Services
Land Clearing
Excavation
Underground Utilities
Environmental Maintenance

The 2 objectives is to market to future clients and to recruit new employees

The sign will be mounted on posts at the entrance of our construction projects
Updates

Low design quality

Target Market(s)

Construction and land developers

Industry/Entity Type

Construction Company

Other font styles liked:
• Hypatia Sans Pro lite

Colors

Designer to choose colors to be used in the design.

Requirements
Must have
• Clean and easy to read
• Civil Construction Services
• Land Clearing
• Excavation
• Underground Utilities
• Road Construction

```html
<!DOCTYPE html>
<html lang="en">
<head>
<meta charset="utf-8">
<title>Harlow Brothers – Now Hiring Site Sign</title>
<link rel="stylesheet" href="https://fonts.googleapis.com/css2?family=Alegreya+Sans:wght@400;500;800&display=swap">
<style>
  :root {
    --backdrop: #e6e6e6;
    --sign-white: #ffffff;
    --brand-blue: #3452a6;
    --brand-blue-light: #5b78c4;
    --rule-blue: #6f86c9;
    --divider-blue: #2d4aa8;
    --footer-grey: #55575c;
    --logo-blue: #3a55a8;
    --sky-top: #dfe9f1;
    --sky-mid: #c9d6e0;
    --site-warm: #d9a673;
    --site-ground: #8c8a86;
  }
  * { margin: 0; padding: 0; box-sizing: border-box; }
  html, body {
    width: 1200px; height: 840px; overflow: hidden;
    background: var(--backdrop);
  }
  .site-sign {
    position: absolute; left: 0; top: 45px;
    width: 1200px; height: 750px;
    background: var(--sign-white);
    overflow: hidden;
    font-family: "Alegreya Sans", sans-serif;
  }
  .site-photo {
    position: absolute; left: 180px; top: 0;
    width: 1020px; height: 652px;
    background:
      linear-gradient(90deg, rgba(255,255,255,1) 0%, rgba(255,255,255,0) 22%),
      linear-gradient(180deg, var(--sky-top) 0%, var(--sky-mid) 42%, var(--site-warm) 72%, var(--site-ground) 100%);
  }
  .hiring-panel {
    position: absolute; left: 57px; top: 0;
    width: 516px; height: 600px;
    background: var(--brand-blue);
    padding: 52px 46px 0 42px;
    color: #fff;
  }
  .hiring-title {
    font-weight: 800;
    font-size: 72px;
    line-height: 80px;
    letter-spacing: 1px;
    padding-left: 6px;
    text-shadow: 3px 4px 6px rgba(0,0,0,0.45);
  }
  .hiring-accent {
    position: absolute; left: 373px; top: 146px;
  }
  .job-list { list-style: none; margin-top: 10px; }
  .job-list li {
    font-weight: 400;
    font-size: 46px;
    line-height: 66px;
    height: 68px;
    border-bottom: 2px solid var(--rule-blue);
    white-space: nowrap;
  }
  .company-name {
    position: absolute; left: 657px; top: 62px;
    display: flex; align-items: center; gap: 22px;
    color: var(--logo-blue);
  }
  .company-name .mark {
    width: 78px; height: 78px;
    background: var(--logo-blue);
  }
  .company-name .wordmark {
    font-weight: 500;
    font-size: 34px;
    line-height: 38px;
    letter-spacing: 3px;
    text-transform: uppercase;
  }
  .services-bar {
    position: absolute; left: 0; top: 652px;
    width: 1200px; height: 98px;
    display: flex; align-items: center; justify-content: center;
    gap: 22px;
    color: var(--footer-grey);
    font-weight: 500;
    font-size: 33px;
  }
  .services-bar .divider {
    width: 4px; height: 42px;
    background: var(--divider-blue);
  }
</style>
</head>
<body>
  <main class="site-sign">
    <div class="site-photo" role="img" aria-label="Photo of a surveyor in a hi-vis vest and hard hat at a construction site with a tower crane and rebar columns at sunset"></div>

    <section class="hiring-panel">
      <h1 class="hiring-title">NOW<br>HIRING!</h1>
      <svg class="hiring-accent" width="48" height="46" viewBox="0 0 48 46" aria-hidden="true">
        <polygon points="0,0 48,0 24,46" fill="var(--brand-blue-light)"/>
      </svg>
      <ul class="job-list">
        <li>Superintendents</li>
        <li>Project Managers</li>
        <li>Pipe Foremen</li>
        <li>Pipe Layers</li>
        <li>Equipment Operators</li>
      </ul>
    </section>

    <div class="company-name">
      <span class="mark" aria-hidden="true"></span>
      <span class="wordmark">Harlow Brothers<br>Civil Construction</span>
    </div>

    <footer class="services-bar">
      <span>Civil Construction Services</span>
      <span class="divider"></span>
      <span>Land Clearing</span>
      <span class="divider"></span>
      <span>Excavation</span>
      <span class="divider"></span>
      <span>Underground Utilities</span>
    </footer>
  </main>
</body>
</html>
```